Banner Ad to promote Youth Cycling Camps

We need a 728 x 90 banner ad to promote some youth cycling camps. There are 2 different camps - a road camp where they learn to ride their bikes on the roads and a mountain bike camp. The camps teach bike handling skills and racing tactics.

Target Market(s)

Parents of youth ages 7-17

Industry/Entity Type

Non-Profit

Font styles to use
Sans Serif

Requirements
Must have
• Logo
• Dates - Road Camp May 5-7, 2017
• - Mountain Bike Camp July 14-16, 2017
• website - quadrapedalcup.org
• be 728 x 90
Nice to have
• Animated - would like it to rotate with 3 slides - 1 a focus on both camps, 1 on road camp, 1 on mountain bike camp

```html
<!DOCTYPE html>
<html lang="en">
<head>
<meta charset="utf-8">
<title>Youth Cycling Camps – Banner Set</title>
<link rel="stylesheet" href="https://fonts.googleapis.com/css2?family=Rubik+Dirt&family=Fjalla+One&family=Lato:wght@700;900&family=Archivo+Black&display=swap">
<style>
  :root {
    --page: #ffffff;
    --ink: #111111;
    --panel-dark: #0e0f0b;
    --panel-mid: #2a2d22;
    --lime: #8cc63f;
    --sky: #6ec6ee;
    --pink: #e0197d;
    --white: #ffffff;
    --logo-ring: #0b0b0b;
    --logo-fill: #5bc2e7;
  }
  * { box-sizing: border-box; margin: 0; padding: 0; }
  html, body {
    width: 1200px; height: 925px; overflow: hidden;
    background: var(--page);
  }
  .sheet { position: relative; width: 1200px; height: 925px; }

  .slide-number {
    position: absolute; left: 0; width: 1200px; text-align: center;
    font-family: "Archivo Black", sans-serif; font-size: 24px; color: var(--ink);
    transform: translateX(11px);
  }

  .banner {
    position: absolute; left: 95px; width: 1016px; height: 126px; overflow: hidden;
    background: linear-gradient(90deg, var(--panel-mid) 0%, var(--panel-dark) 45%, #1c1e17 75%, var(--panel-dark) 100%);
  }

  .photo { position: absolute; top: 0; height: 126px; }
  .photo--trail-a { left: 0; width: 260px; clip-path: polygon(0 0, 184px 0, 247px 126px, 0 126px);
    background: linear-gradient(160deg, #6f6a4d 0%, #9c8c63 45%, #c9b592 100%); }
  .photo--trail-b { left: 190px; width: 260px; clip-path: polygon(0 0, 260px 0, 260px 126px, 64px 126px);
    background: linear-gradient(180deg, #3e4a33 0%, #66704f 50%, #b9ab8a 100%); }
  .photo--coach-a { left: 0; width: 260px; clip-path: polygon(0 0, 184px 0, 247px 126px, 0 126px);
    background: linear-gradient(170deg, #2f3a2a 0%, #4d5a3a 55%, #7d7a5a 100%); }
  .photo--coach-b { left: 190px; width: 260px; clip-path: polygon(0 0, 260px 0, 260px 126px, 64px 126px);
    background: linear-gradient(180deg, #24301f 0%, #4f6a3a 50%, #8b9a6a 100%); }
  .photo--group { left: 0; width: 430px;
    background: linear-gradient(180deg, #c9cdd2 0%, #b6bcc3 35%, #6d4f5a 55%, #3e4a6a 75%, #8a8a60 100%); }

  .backdrop { position: absolute; top: 0; left: 430px; width: 586px; height: 126px;
    background: linear-gradient(90deg, rgba(60,66,50,.55), rgba(20,22,16,.2) 60%, rgba(40,44,34,.4)); }

  .brand {
    position: absolute; top: 9px; left: 380px; width: 108px; height: 108px; border-radius: 50%;
    background: var(--logo-fill); border: 6px solid var(--logo-ring);
    display: flex; align-items: center; justify-content: center; text-align: center;
  }
  .brand__name {
    font-family: "Fjalla One", sans-serif; font-size: 15px; line-height: 1.05;
    color: var(--logo-ring); text-transform: uppercase; letter-spacing: .5px;
  }

  .copy {
    position: absolute; top: 0; left: 500px; width: 510px; height: 126px;
    display: flex; flex-direction: column; justify-content: center; align-items: center; text-align: center;
  }
  .headline {
    font-family: "Rubik Dirt", sans-serif; color: var(--lime);
    font-size: 31px; line-height: 1.08; white-space: nowrap;
  }
  .headline--small { font-size: 25px; line-height: 1.18; }
  .quote {
    font-family: "Fjalla One", sans-serif; color: var(--sky);
    font-size: 26px; line-height: 1.2; margin-top: 3px; white-space: nowrap;
  }
  .copy--dates { align-items: flex-start; text-align: left; left: 515px; width: 500px; }
  .dates { font-family: "Fjalla One", sans-serif; color: var(--lime); font-size: 30px; line-height: 1.22; white-space: nowrap; }
  .quote--small { font-size: 19px; margin-top: 4px; }

  .web-tag {
    position: absolute; left: 0; bottom: 7px; height: 31px; padding: 0 14px 0 8px;
    background: var(--pink); color: var(--white);
    font-family: "Lato", sans-serif; font-weight: 900; font-size: 18px; line-height: 31px;
  }
</style>
</head>
<body>
<main class="sheet">

  <div class="slide-number" style="top:96px">1</div>
  <section class="banner" style="top:144px" aria-label="Slide 1: both camps">
    <div class="photo photo--trail-a" role="img" aria-label="Young riders descending a dirt trail on mountain bikes"></div>
    <div class="photo photo--trail-b" role="img" aria-label="Youth cyclists riding a forest road"></div>
    <div class="backdrop" role="img" aria-label="Faded photo of a rider in the woods"></div>
    <div class="brand"><span class="brand__name">Quadrapedal<br>Cup</span></div>
    <div class="copy">
      <h2 class="headline">Best Cycling Camps for Youth<br>Ages 7-17</h2>
      <p class="quote">Good mix of skill building exercises and just riding</p>
    </div>
  </section>

  <div class="slide-number" style="top:352px">2</div>
  <section class="banner" style="top:399px" aria-label="Slide 2: coaching">
    <div class="photo photo--coach-a" role="img" aria-label="Young riders on a forest path with a coach"></div>
    <div class="photo photo--coach-b" role="img" aria-label="Coach riding alongside a young cyclist"></div>
    <div class="backdrop" role="img" aria-label="Faded photo of a coach"></div>
    <div class="web-tag">quadrapedalcup.org</div>
    <div class="brand"><span class="brand__name">Quadrapedal<br>Cup</span></div>
    <div class="copy">
      <h2 class="headline headline--small">Professional Coaches,<br>great youth to adult ratio, affordable</h2>
      <p class="quote">Well organized, great coaches, good location</p>
    </div>
  </section>

  <div class="slide-number" style="top:607px">3</div>
  <section class="banner" style="top:654px" aria-label="Slide 3: camp dates">
    <div class="photo photo--group" role="img" aria-label="Group photo of camp riders and coaches outdoors"></div>
    <div class="backdrop" role="img" aria-label="Faded photo of riders in a field"></div>
    <div class="web-tag">quadrapedalcup.org</div>
    <div class="brand"><span class="brand__name">Quadrapedal<br>Cup</span></div>
    <div class="copy copy--dates">
      <p class="dates">Road Camp – May 5-7, 2017<br>Mountain Bike Camp – July 14-16, 2017</p>
      <p class="quote quote--small">So thankful that these camps are affordable for families like ours!</p>
    </div>
  </section>

</main>
</body>
</html>
```